CalmVisit Homepage and Landing Pages

Please see detailed brief.

CalmVisit is Australia’s newest online therapy and mental health service. We allow patients from across australia to connect with Mental health practitioners from across Australia. Our mission is to remove the friction in gaining support for mental health related issues.

Number of Pages Required

1 page

Font styles to use
Sans Serif

Colors
33a6d7
0293ce
3277b5
0255a3
acd136
9bcb3c

Requirements
Must have
• Please see detailed brief.
Nice to have
• Please see detailed brief
Should not have

```html
<!DOCTYPE html>
<html lang="en">
<head>
<meta charset="utf-8">
<title>CalmVisit — Online Mental Health Care</title>
<link href="https://fonts.googleapis.com/css2?family=Montserrat:wght@300;400;500;600&display=swap" rel="stylesheet">
<style>
:root{
  --blue:#3b7ddb;
  --blue-dark:#2f66b8;
  --navy:#2c4a72;
  --ink:#333a44;
  --muted:#8a8f97;
  --line:#d6d9de;
  --field:#c9ccd1;
  --band:#efefef;
  --quote:#e3e6ec;
  --icon-fill:#dbe7f8;
}
*{box-sizing:border-box;margin:0;padding:0}
html,body{width:1200px;height:3800px;overflow:hidden}
body{position:relative;background:#fff;font-family:'Montserrat',sans-serif;color:var(--ink)}
.abs{position:absolute}
.center{text-align:center}
a{color:inherit;text-decoration:none}

/* header */
.top-links{left:90px;top:42px;font-size:10px;display:flex;gap:16px}
.brand{left:0;width:1200px;top:26px;display:flex;justify-content:center;align-items:center;gap:12px;font-size:38px;font-weight:400;color:var(--navy)}
.brand-dot{width:26px;height:26px;border-radius:50%;background:var(--blue)}
.btn-login{left:946px;top:35px;width:75px;height:30px;border:1.5px solid var(--blue);color:var(--blue);font-size:10px;display:flex;align-items:center;justify-content:center}
.btn-signup{left:1034px;top:35px;width:75px;height:30px;background:var(--blue);color:#fff;font-size:10px;display:flex;align-items:center;justify-content:center}
.headline{left:0;width:1200px;top:142px;font-size:23px;line-height:34px;font-weight:400}
.intro{left:350px;width:500px;top:236px;font-size:11px;line-height:16px;color:#555}
.main-nav{top:354px;left:0;width:1200px;font-size:11px}
.main-nav span{position:absolute}

/* hero */
.hero{left:0;top:394px;width:1200px;height:411px;background:linear-gradient(180deg,#8ca2b4 0%,#6f8ea6 28%,#5a7d95 45%,#b7a68f 62%,#c8b69c 100%)}
.hero-btn{left:514px;top:554px;width:164px;height:43px;background:var(--blue);color:#fff;font-size:10px;display:flex;align-items:center;justify-content:center}
.dots{display:flex;gap:5px}
.dot{width:6px;height:6px;border-radius:50%;border:1px solid #fff}
.dot.on{background:#fff}

/* sections */
.h2{left:0;width:1200px;font-size:23px;font-weight:400;letter-spacing:.5px}
.lead{font-size:11px;line-height:16px;color:var(--muted)}
.step-icon{width:92px;height:96px;border-radius:8px;background:var(--icon-fill)}
.step{width:290px}
.step-title{font-size:15px;font-weight:400;margin-bottom:18px;text-align:left;padding-left:34px}
.step-title b{color:var(--blue);font-weight:500;margin-right:12px}
.step p{font-size:11px;line-height:16px;color:var(--muted);text-align:center}
.tagline{left:0;width:1200px;top:1443px;font-size:14.5px;line-height:23px;letter-spacing:.6px}
.arrow-btn{width:40px;height:40px;background:#c4d8f5;display:flex;align-items:center;justify-content:center}

.prac-photo{width:241px;height:176px}
.prac-name{position:absolute;left:0;right:0;bottom:30px;color:#fff;font-size:15px;text-align:center}
.prac-role{position:absolute;left:0;right:0;bottom:12px;color:var(--blue);font-size:11px;text-align:center}
.prac-info{width:245px;font-size:11.5px;line-height:16px}
.prac-info h4{font-size:11.5px;font-weight:500}
.prac-info small{display:block;font-size:8px;color:#555;margin-bottom:8px}
.cta{height:43px;width:164px;font-size:10px;display:flex;align-items:center;justify-content:center}
.cta.solid{background:var(--blue);color:#fff}
.cta.outline{border:1.5px solid var(--blue);color:var(--blue)}
.rule{left:0;width:1200px;height:1px;background:var(--line)}

.quote-mark{font-size:150px;color:var(--quote);font-family:Georgia,serif;line-height:1}
.avatar{width:70px;height:70px;border-radius:50%;background:radial-gradient(circle at 50% 40%,#c9a088,#6b4a3a)}

/* team */
.team-card{position:absolute;color:#fff}
.team-photo{position:absolute;left:0;top:0;width:100%}
.team-text{position:absolute;left:27px;right:27px}
.team-text h3{font-size:19px;font-weight:400;line-height:20px}
.team-text i{display:block;width:12px;height:5px;background:var(--blue);margin:4px 0 10px}
.team-text p{font-size:9.5px;line-height:14px}
.team-btn{position:absolute;left:0;width:100%;background:var(--blue);color:#fff;font-size:9.5px;display:flex;align-items:center;justify-content:center}

/* contact */
.contact-band{left:0;top:2839px;width:1200px;height:547px;background:var(--band)}
.label{font-size:13px;left:385px}
.field{left:383px;width:432px;border:2px solid var(--field);background:transparent;font-size:11px;color:#aaa;padding:17px 18px;line-height:16px}
.send{left:519px;top:3287px;width:162px;height:41px;background:var(--blue);color:#fff;font-size:9.5px;display:flex;align-items:center;justify-content:center}

/* footer */
.footer{left:0;top:3386px;width:1200px;height:414px;background:var(--navy);color:#fff}
.f-brand{left:90px;top:3445px;font-size:36px;display:flex;align-items:center;gap:12px}
.f-brand .brand-dot{background:#fff;width:24px;height:24px}
.f-head{font-size:15px;letter-spacing:.5px;top:3533px}
.f-link{font-size:10.5px;width:189px;padding-bottom:6px}
.f-link.ul{border-bottom:1px solid rgba(255,255,255,.7)}
.social-sq{width:26px;height:26px;background:#fff;border-radius:3px}
.chat-box{left:870px;top:3538px;width:238px;height:51px;border:1.5px solid #fff;display:flex;align-items:center;gap:10px;padding-left:10px;font-size:10.5px;line-height:15px}
.legal{top:3738px;font-size:10.5px}
</style>
</head>
<body>

<!-- header -->
<nav class="abs top-links"><a>Find a Practioner</a><a>Become a Practioner</a></nav>
<div class="abs brand"><span class="brand-dot"></span>CalmVisit</div>
<a class="abs btn-login">Login</a>
<a class="abs btn-signup">Sign Up</a>

<h1 class="abs headline center" style="font-weight:400">Getting access to mental health treatments doesn’t<br>have to be stresfull.</h1>
<p class="abs intro center">We provides on-demand access to a range of psychologists &amp; personal<br>wellness professionals from across Australia.&nbsp; Book your online<br>appointment in minutes, 24/7.</p>

<nav class="abs main-nav">
  <span style="left:287px">Home</span>
  <span style="left:415px">How it Works</span>
  <span style="left:582px">Meet Our Team</span>
  <span style="left:760px">Contact</span>
  <svg class="abs" style="left:899px;top:2px" width="12" height="12" viewBox="0 0 12 12"><circle cx="5" cy="5" r="3.8" fill="none" stroke="#333" stroke-width="1.2"/><line x1="8" y1="8" x2="11" y2="11" stroke="#333" stroke-width="1.2"/></svg>
</nav>

<!-- hero -->
<div class="abs hero" role="img" aria-label="Photo of two blue wooden beach chairs on the sand facing a calm sea"></div>
<a class="abs hero-btn">Find a Practitioner</a>
<div class="abs dots" style="left:586px;top:770px"><span class="dot on"></span><span class="dot"></span><span class="dot"></span></div>

<!-- why -->
<h2 class="abs h2 center" style="top:862px">Why CalmVisit</h2>
<p class="abs lead center" style="left:400px;width:400px;top:920px">We want to break down the barriers in receiving effective<br>treatment and care for anxiety, stress and mental health<br>related issues.</p>

<!-- how it works -->
<h2 class="abs h2 center" style="top:1027px">How It Works</h2>

<div class="abs step-icon" style="left:244px;top:1112px" role="img" aria-label="Illustration of a phone with a magnifying glass"></div>
<div class="abs step-icon" style="left:549px;top:1112px" role="img" aria-label="Illustration of a doctor with a stethoscope"></div>
<div class="abs step-icon" style="left:859px;top:1112px" role="img" aria-label="Illustration of a phone with a chat bubble and list"></div>

<div class="abs step" style="left:144px;top:1228px"><div class="step-title" style="padding-left:44px"><b>01</b>Find a Practitioner</div><p>Search for health professional that best suits<br>your circumstances from anywhere in<br>Australia. Physical location is no longer a<br>barrier. Consultations are conducted online<br>via video or voice call.</p></div>
<div class="abs step" style="left:450px;top:1228px"><div class="step-title" style="padding-left:32px"><b>02</b>Book an Appointment</div><p>Book an online appointment at<br>a time that suits you. 24/7 and<br>365 days a year.</p></div>
<div class="abs step" style="left:767px;top:1228px"><div class="step-title" style="padding-left:9px"><b>03</b>Chat with your Consultant</div><p>When it’s time for your consultation, simply<br>log in and start your session. You have the<br>option of conducting a voice only or video call.<br>It’s up to you..</p></div>

<p class="abs tagline center">Get treatment for anxiety &amp; depression from your home or<br>workplace. 100% online. No travel. No clinics.</p>

<div class="abs arrow-btn" style="left:1017px;top:1529px"><svg width="14" height="12" viewBox="0 0 14 12" fill="none" stroke="#fff" stroke-width="1.5"><path d="M13 6H2M6 1L1 6l5 5"/></svg></div>
<div class="abs arrow-btn" style="left:1069px;top:1529px"><svg width="14" height="12" viewBox="0 0 14 12" fill="none" stroke="#fff" stroke-width="1.5"><path d="M1 6h11M8 1l5 5-5 5"/></svg></div>

<!-- practitioners -->
<div class="abs prac-photo" style="left:90px;top:1589px;background:linear-gradient(180deg,#8fa3ad,#5d6e76 60%,#2d3538)" role="img" aria-label="Portrait photo of a practitioner with auburn hair by a lake">
  <div class="prac-name">Nora Hale</div><div class="prac-role">General Psychologist</div>
</div>
<div class="abs prac-info" style="left:348px;top:1614px">
  <h4>Experience</h4><small>4 years</small>
  <h4>Available</h4><small>10 Sept, 9:00 am</small>
  I am an experience Psychologist who<br>has great empathy and compasion for<br>my clients. I have more than ten years<br>clinical experience in both the mental<br>health and disability sector.
</div>
<div class="abs prac-photo" style="left:643px;top:1589px;background:linear-gradient(180deg,#9a8f84,#6d6258 55%,#2f2c2a)" role="img" aria-label="Portrait photo of a bearded practitioner in front of a brick wall">
  <div class="prac-name">Owen Marsh</div><div class="prac-role">General Psychologist</div>
</div>
<div class="abs prac-info" style="left:902px;top:1614px;width:210px">
  <h4>Experience</h4><small>4 years</small>
  <h4>Available</h4><small>10 Sept, 9:00 am</small>
  I am an experience Psychologist<br>who has great empathy and<br>compasion for my clients. I have<br>more than ten years clinical<br>experience .
</div>

<div class="abs dots" style="left:570px;top:1816px">
  <span class="dot" style="border-color:var(--blue)"></span><span class="dot" style="border-color:var(--blue)"></span><span class="dot" style="border-color:var(--blue)"></span><span class="dot on" style="border-color:var(--blue);background:var(--blue)"></span><span class="dot" style="border-color:var(--blue)"></span><span class="dot" style="border-color:var(--blue)"></span>
</div>

<a class="abs cta solid" style="left:432px;top:1845px">Find a Practitioner</a>
<a class="abs cta outline" style="left:604px;top:1845px">Become a Practitioner</a>

<div class="abs rule" style="top:1934px"></div>

<!-- testimonials -->
<h2 class="abs h2 center" style="top:2019px">Happy Patients</h2>
<div class="abs quote-mark" style="left:326px;top:2030px">“</div>
<div class="abs quote-mark" style="left:772px;top:2072px">”</div>
<p class="abs center" style="left:428px;width:344px;top:2083px;font-size:11px;line-height:16px">Lorem ipsum dolor sit amet, consectetur adipiscing<br>elit, sed do eiusmod tempor incididunt ut labore et<br>dolore magna aliqua.</p>
<div class="abs avatar" style="left:522px;top:2177px" role="img" aria-label="Photo of the patient"></div>
<div class="abs" style="left:607px;top:2205px;font-size:14px;color:#555">Clara</div>

<div class="abs rule" style="top:2294px"></div>

<!-- team -->
<h2 class="abs h2 center" style="top:2325px">Meet Our Team</h2>

<div class="team-card" style="left:156px;top:2448px;width:257px;height:273px">
  <div class="team-photo" style="height:232px;background:linear-gradient(180deg,#3a3330,#1c1a19)" role="img" aria-label="Portrait photo of an older team member in a dark suit"></div>
  <div class="team-text" style="top:122px"><h3>Dr. Peter<br>Vance</h3><i></i><p>Dr Peter Vance is an Australian neuroscientist in private practice specializing in brain performance.</p></div>
  <div class="team-btn" style="top:232px;height:41px">Read more</div>
</div>
<div class="team-card" style="left:450px;top:2425px;width:303px;height:317px">
  <div class="team-photo" style="height:274px;background:linear-gradient(180deg,#8a8a80,#5d5f58 60%,#3e403c)" role="img" aria-label="Portrait photo of a smiling team member seated at a desk"></div>
  <div class="team-text" style="top:144px;right:70px"><h3>Dr. Ella<br>Grant</h3><i></i><p>This is just a placeholder text to give short information about the image.</p></div>
  <div class="team-btn" style="top:274px;height:43px;font-size:10px">Read more</div>
</div>
<div class="team-card" style="left:789px;top:2448px;width:257px;height:273px">
  <div class="team-photo" style="height:232px;background:linear-gradient(180deg,#a7a9ab,#6d6f71 60%,#3b3c3d)" role="img" aria-label="Portrait photo of a grey-haired team member wearing glasses"></div>
  <div class="team-text" style="top:122px;right:60px"><h3>Dr. Martin<br>Cole</h3><i></i><p>This is just a placeholder text to give short information about the image.</p></div>
  <div class="team-btn" style="top:232px;height:41px">Read more</div>
</div>

<!-- contact -->
<section class="abs contact-band" role="img" aria-label="Faint world map backdrop"></section>
<h2 class="abs h2 center" style="top:2870px">Contact</h2>
<div class="abs label" style="top:2932px">Name</div>
<div class="abs field" style="top:2963px;height:51px">Your name goes here</div>
<div class="abs label" style="top:3032px">Email</div>
<div class="abs field" style="top:3062px;height:53px">Your email goes here</div>
<div class="abs label" style="top:3132px;left:383px">Message</div>
<div class="abs field" style="top:3162px;height:91px;padding-top:22px">Get in touch with us and tell us what’s<br>on your mind</div>
<a class="abs send">Send to Us</a>

<!-- footer -->
<footer class="abs footer"></footer>
<div class="abs f-brand" style="color:#fff"><span class="brand-dot"></span>CalmVisit</div>
<div class="abs" style="right:90px;top:3446px;font-size:14px;color:#fff;letter-spacing:.5px">Social Media</div>
<div class="abs social-sq" style="left:1045px;top:3473px"></div>
<div class="abs social-sq" style="left:1084px;top:3473px"></div>

<div class="abs f-head" style="left:90px;color:#fff">For Patient</div>
<div class="abs f-head" style="left:367px;color:#fff">For Practitioner</div>
<div class="abs f-head" style="left:659px;color:#fff">Contents</div>

<div class="abs f-link ul" style="left:90px;top:3580px;color:#fff">Find a Practitioner</div>
<div class="abs f-link ul" style="left:90px;top:3618px;color:#fff">Pay my bil</div>
<div class="abs f-link ul" style="left:367px;top:3580px;color:#fff">Become a Practitioner</div>
<div class="abs f-link ul" style="left:367px;top:3618px;color:#fff">Refer a patient</div>
<div class="abs f-link ul" style="left:367px;top:3655px;color:#fff">Transfer a patient</div>
<div class="abs f-link" style="left:659px;top:3580px;color:#fff">Home</div>
<div class="abs f-link" style="left:659px;top:3618px;color:#fff">How It Works</div>
<div class="abs f-link" style="left:659px;top:3655px;color:#fff">Meet Our Team</div>

<div class="abs chat-box" style="color:#fff">
  <svg width="26" height="20" viewBox="0 0 26 20" fill="none" stroke="#fff" stroke-width="1.3"><rect x="1" y="1" width="17" height="12" rx="2"/><path d="M5 13v4l4-4"/><path d="M20 6h4v10h-3v3l-3-3h-6v-2"/><circle cx="6" cy="7" r=".8" fill="#fff"/><circle cx="9.5" cy="7" r=".8" fill="#fff"/><circle cx="13" cy="7" r=".8" fill="#fff"/></svg>
  <div>Let’s Chat!<br>We’ll reply as soon as possible</div>
</div>

<div class="abs legal" style="left:88px;color:#fff">© 2020 CalmVisit. All Rights Reserved.</div>
<div class="abs legal" style="left:591px;color:#fff">Help &amp; FAQ</div>
<div class="abs legal" style="left:733px;color:#fff">Privacy Policy</div>
<div class="abs legal" style="left:883px;color:#fff">Terms &amp; Conditions</div>
<div class="abs legal" style="right:90px;color:#fff">Contact</div>

</body>
</html>
```